Verpackungen für Entwicklung von innovativen Lebensmitteln mit exotischen Zutatenkombinationen
Zielgruppe
Entwicklung, Produktion und Vertrieb von neuartigen und innovativen Lebensmitteln mit exotischen Zutatenkombinationen.
Zielgruppe ist zwischen 18 und 55 Jahre alt, single und berufstätig. Unsere Zielgruppe lebt ernährungsbewusst, treibt Sport(amateur, semi-professionell und professionell ) & ist interessiert an einem gesunden Lebensstil.
Aufgabenstellung
Unser Produkt, das am besten mit Porridge/Müsli zu vergleichen wäre wird in einem 350ml Glas verpackt - ähnlich wie ein Marmeladenglas.
Das Design das wir benötigen, ist für die Banderole welches auf dieses Glas gestülpt wird. Zu der Verpackung gehört auch ein Etikett, welches auf dem Deckel aufgeklebt (Rund, Durchmesser 6,9cm) und diesen mit dem Glas verbindet - Siehe Vorstellung im Anhang.
Da wir 4 Geschmacksrichtungen haben, benötigen wir auch 4 unterschiedliche Designs. Diese sollen sich jedoch nur farblich unterschieden.
Die Bezeichnung des Produktes lautet Kraftkorn & Eiweiß Flitzer, 1. Geschmacksrichtung - Sunda Sturm, 2. Geschmacksrichtung - Lilly Frilly, 3. Geschmacksrichtung - Rund um Kerne und die 4. Geschmacksrichtung - Pear Cardamom.
Im Anhang befindet sich noch Bilddateien mit unserem Logo, dieses soll auf das Deckel-Etikett. Auch dessen Farbe soll je Geschmacksrichtung unterschiedlich sein. Die Dateien im Anhang dienen nur als Veranschaulichung. Bei der Frabgestaltung haben Sie auch freie Wahl.
Wir wünschen uns ein Retro/Vintage-Design - jedoch nicht zu übertrieben.

```html
<!DOCTYPE html>
<html lang="de">
<head>
<meta charset="utf-8">
<title>Kraftkorn &amp; Eiweiß Flitzer – Banderole Sunda Sturm</title>
<link rel="stylesheet" href="https://fonts.googleapis.com/css2?family=Amatic+SC:wght@700&family=Caveat+Brush&display=swap">
<style>
  :root {
    --paper: #ffffff;
    --cream: #f6f1c0;
    --cream-deep: #efe7a8;
    --teal: #13a88b;
    --mint: #a9d6bc;
    --mint-deep: #6fbf9f;
    --ink: #151515;
    --sketch: #8a8a78;
  }
  html, body {
    margin: 0;
    padding: 0;
    width: 1200px;
    height: 848px;
    overflow: hidden;
    background: var(--paper);
  }
  .packaging { display: block; width: 1200px; height: 848px; }
  .band-fill { fill: var(--cream); }
  .sun-disc { fill: var(--mint); }
  .sun-disc-overlap { fill: var(--mint-deep); }
  .illustration { fill: var(--sketch); opacity: .35; }
  .product-title {
    font-family: "Amatic SC", "Arial Narrow", sans-serif;
    font-weight: 700;
    font-size: 40px;
    fill: var(--ink);
    text-anchor: middle;
  }
  .flavour-ribbon { fill: var(--ink); }
  .flavour-name {
    font-family: "Caveat Brush", cursive;
    font-size: 26px;
    fill: var(--cream);
    text-anchor: middle;
  }
  .lid-label { fill: var(--cream); stroke: var(--teal); stroke-width: 12; }
  .brand-disc { fill: var(--ink); }
  .brand-name {
    font-family: "Amatic SC", "Arial Narrow", sans-serif;
    font-weight: 700;
    fill: var(--cream);
    text-anchor: middle;
  }
  .lid-ring-text {
    font-family: "Amatic SC", "Arial Narrow", sans-serif;
    font-weight: 700;
    font-size: 27px;
    fill: var(--ink);
    letter-spacing: .5px;
  }
  .lid-flavour {
    font-family: "Caveat Brush", cursive;
    font-size: 25px;
    fill: var(--ink);
    text-anchor: middle;
  }
</style>
</head>
<body>
<svg class="packaging" viewBox="0 0 1200 848" xmlns="http://www.w3.org/2000/svg">
  <defs>
    <clipPath id="band-shape">
      <path d="M152 391 Q640 366 1132 391 L1118 685 Q640 668 170 682 Z"/>
    </clipPath>
    <path id="lid-ring" d="M544 167 A106 106 0 1 1 756 167 A106 106 0 1 1 544 167"/>
  </defs>

  <!-- Banderole -->
  <g class="banderole" clip-path="url(#band-shape)">
    <rect class="band-fill" x="140" y="360" width="1000" height="340"/>
    <circle class="sun-disc" cx="540" cy="770" r="330"/>
    <path class="sun-disc-overlap" d="M400 700 Q430 560 560 560 Q720 560 760 700 Z"/>
    <rect class="illustration" x="350" y="420" width="250" height="270" rx="40"
          role="img" aria-label="Skizzierter Flamingo"/>
    <rect class="illustration" x="740" y="440" width="300" height="250" rx="40"
          role="img" aria-label="Skizzierter Pelikan"/>
  </g>

  <text class="product-title" x="661" y="550">Kraftkorn &amp;</text>
  <text class="product-title" x="661" y="592">Eiweiß Flitzer</text>

  <g class="flavour-banner">
    <path class="flavour-ribbon" d="M579 610 L741 610 L732 626 L741 643 L579 643 L588 626 Z"/>
    <text class="flavour-name" x="660" y="635">Sunda Sturm</text>
  </g>

  <!-- Deckel-Etikett mit Lasche -->
  <g class="lid-tab">
    <path class="lid-label" d="M623 290 L623 400 A45 45 0 1 0 681 400 L681 290 Z"/>
    <circle class="lid-label" cx="650" cy="167" r="137"/>
    <rect x="629" y="280" width="46" height="125" fill="var(--cream)"/>
    <circle cx="652" cy="440" r="39" fill="var(--cream)"/>
    <circle class="brand-disc" cx="652" cy="440" r="34"/>
    <text class="brand-name" x="652" y="448" font-size="22">Nova Korn</text>

    <text class="lid-ring-text">
      <textPath href="#lid-ring" startOffset="25%" text-anchor="middle">Kraftkorn &amp; Eiweiß Flitzer</textPath>
    </text>
    <text class="lid-ring-text">
      <textPath href="#lid-ring" startOffset="75%" text-anchor="middle">Kraftkorn &amp; Eiweiß Flitzer</textPath>
    </text>
    <text class="lid-flavour" x="570" y="176">sunda</text>
    <text class="lid-flavour" x="735" y="176">sturm</text>

    <circle class="brand-disc" cx="650" cy="167" r="38"/>
    <text class="brand-name" x="650" y="175" font-size="24">Nova Korn</text>
  </g>
</svg>
</body>
</html>
```